Brambleton Resource Holdings, LP Letter Head

We need an official company letter head design that is clean and mimics our company logo style. It will include our logo, address, phone, and website. We are an OIl and Gas mineral purchasing company, so hints of oil rigs or related design would be desirable.

Industry/Entity Type

Oil And Gas

Colors
ec1f27
f04a50
f59195
fbd4d5

Requirements
Must have
• Logo
• 7392 Whitcombe R. Ashdale Parkway, Suite 618
• Dallas TX, 75391
• 214-673-1958
• www.bramblestoneres.example
Nice to have
• Oil Rigs or OIl and gas related design

```html
<!DOCTYPE html>
<html lang="en">
<head>
<meta charset="utf-8">
<title>Brambleton Resource Holdings, LP – Letterhead</title>
<link rel="stylesheet" href="https://fonts.googleapis.com/css2?family=Questrial&display=swap">
<style>
  :root {
    --red: #ec1f27;
    --red-deep: #d41920;
    --red-soft: #f59195;
    --red-pale: #fbd4d5;
    --paper: #ffffff;
    --ink: #4a4a4a;
    --backdrop: #dcccb2;
  }
  * { box-sizing: border-box; margin: 0; padding: 0; }
  html, body {
    width: 1200px; height: 893px; overflow: hidden;
    background: var(--backdrop);
    font-family: "Questrial", sans-serif;
  }
  .letterhead {
    position: absolute; left: 270px; top: 20px;
    width: 660px; height: 853px;
    background: var(--paper);
    overflow: hidden;
    box-shadow: 0 6px 24px rgba(0,0,0,.12);
  }
  .band-vertical {
    position: absolute; left: 40px; top: 0; width: 60px; height: 100%;
    background: var(--red);
  }
  .band-top-left {
    position: absolute; left: 40px; top: 85px; width: 240px; height: 52px;
    background: var(--red);
  }
  .band-top-right {
    position: absolute; left: 510px; top: 60px; width: 150px; height: 52px;
    background: var(--red);
  }
  .logo-square {
    position: absolute; left: 48px; top: 89px; width: 44px; height: 44px;
    border: 2px solid var(--paper);
  }
  .brand-name {
    position: absolute; left: 298px; top: 88px;
    color: var(--red); font-size: 19px; line-height: 22px;
    letter-spacing: .5px;
  }
  .letter-body {
    position: absolute; left: 150px; top: 190px; width: 440px;
    color: var(--ink); font-size: 11.5px; line-height: 19px;
    text-align: justify;
  }
  .letter-body p + p { margin-top: 30px; }
  .rig-scene {
    position: absolute; left: 270px; bottom: 0; width: 390px; height: 250px;
    background: linear-gradient(to bottom, rgba(251,212,213,0) 0%, rgba(251,212,213,.55) 55%, var(--red-pale) 100%);
  }
  .signature {
    position: absolute; left: 480px; top: 640px; color: var(--ink);
  }
  .signature-name { font-size: 13px; }
  .signature-title { font-size: 9px; margin-top: 2px; }
  .contact {
    position: absolute; left: 290px; top: 760px; width: 330px;
    color: var(--ink); font-size: 10.5px;
  }
  .contact-row { display: flex; justify-content: space-between; align-items: center; }
  .contact-item { display: flex; align-items: center; gap: 6px; }
  .contact-icon { width: 12px; height: 12px; }
  .contact-rule { height: 1.5px; background: var(--red); margin: 6px 0 5px; }
  .contact-address { text-align: center; }
</style>
</head>
<body>
  <main class="letterhead">
    <div class="band-vertical"></div>
    <div class="band-top-left"></div>
    <div class="band-top-right"></div>
    <div class="logo-square"></div>
    <div class="brand-name">Brambleton<br>Resource Holdings</div>

    <section class="letter-body">
      <p>Lorem ipsum dolor sit amet, consectetur adipiscing elit. Donec orci purus, luctus vitae dignissim eu, iaculis sed purus. Vivamus faucibus, ipsum nec aliquet viverra, leo mauris condimentum ligula, sit amet sagittis enim ligula quis arcu. Nam egestas tortor id nisl porttitor mattis. In tortor ante, ultricies in suscipit a, tempus non massa.</p>
      <p>Lorem ipsum dolor sit amet, consectetur adipiscing elit. Donec orci purus, luctus vitae dignissim eu, iaculis sed purus. Vivamus faucibus, ipsum nec aliquet viverra, leo mauris condimentum ligula, sit amet sagittis enim ligula quis arcu. Nam egestas tortor id nisl porttitor mattis. In tortor ante, ultricies in suscipit a, tempus non massa.</p>
      <p>Morbi semper magna eget tincidunt semper, odio nibh rutrum mi, id feugiat ante nisl eu risus. Cras mattis varius eros, vel fringilla nisl suscipit eget. Quisque scelerisque sagittis nulla at porttitor. Mauris a justo et tellus interdum tristique.</p>
      <p>Aliquam faucibus ultricies sem, id tincidunt gravida arcu adipiscing lacus, ac bibendum nulla leo eu purus. Donec eu magna a metus ornare faucibus. Fusce aliquet faucibus ultricies. Vestibulum id purus lorem.</p>
    </section>

    <div class="rig-scene" role="img" aria-label="Faint pink silhouettes of oil derricks and pumpjacks along the bottom of the page"></div>

    <div class="signature">
      <div class="signature-name">Aldous Penhale</div>
      <div class="signature-title">Co-Founder &amp; CEO</div>
    </div>

    <footer class="contact">
      <div class="contact-row">
        <span class="contact-item">
          <svg class="contact-icon" viewBox="0 0 12 12" aria-hidden="true">
            <circle cx="6" cy="6" r="6" fill="var(--red)"/>
            <path d="M3.8 3.2c.4-.3.8-.2 1 .2l.5.9c.2.3.1.6-.2.8l-.3.2c.3.7.9 1.3 1.6 1.6l.2-.3c.2-.3.5-.4.8-.2l.9.5c.4.2.5.6.2 1-.6.8-1.5.9-2.5.3-1-.6-1.9-1.5-2.5-2.5-.6-1-.5-1.9.3-2.5z" fill="#fff"/>
          </svg>
          214-673-1958
        </span>
        <span class="contact-item">
          <svg class="contact-icon" viewBox="0 0 12 12" aria-hidden="true">
            <circle cx="6" cy="6" r="6" fill="var(--red)"/>
            <circle cx="6" cy="6" r="3.3" fill="none" stroke="#fff" stroke-width=".9"/>
            <path d="M2.7 6h6.6M6 2.7c-1.5 1.8-1.5 4.8 0 6.6M6 2.7c1.5 1.8 1.5 4.8 0 6.6" fill="none" stroke="#fff" stroke-width=".7"/>
          </svg>
          www.bramblestoneres.example
        </span>
      </div>
      <div class="contact-rule"></div>
      <div class="contact-address">7392 Whitcombe R. Ashdale Parkway, Suite 618 Dallas TX, 75391</div>
    </footer>
  </main>
</body>
</html>
```